marla verstegen
chef
marla verstegen - Chef / Catering
Creative Brief
Use specific fonts
may mix logo font with another font, both must be free and downloadable
Simple
professional chef
none
marla@marlaverstegen.net
marlaverstegen.net
For the biz cards: on the flip side, my social media info: website: marlaverstegen.net twitter: @marlaverstegen facebook: facebook.com/marla.verstegen blog: www.ourfinaldinnertable.net I'd like to have the symbols rather than words for social media I would like to have a folded card for thank yous and notes on the back of the envelope place the logo, then underneath: 518 tuckaway st. denver, co 80219 I would like the theme of the stars in the logo to be pulled through the products
website: marlaverstegen.net twitter: @marlaverstegen facebook: facebook.com/marla.verstegen blog: ourfinaldinnertable.net

```html
<!DOCTYPE html>
<html lang="en">
<head>
<meta charset="utf-8">
<title>marla verstegen — business cards</title>
<link rel="stylesheet" href="https://fonts.googleapis.com/css2?family=Oswald:wght@400&family=Open+Sans:wght@400;600&display=swap">
<style>
  :root {
    --bg: #e8e4df;
    --card: #ffffff;
    --red: #b3282d;
    --red-dark: #8e1c20;
    --grey-light: #cfcfcf;
    --text-grey: #6d6d6d;
    --pink: #e7a3a5;
  }
  * { margin: 0; padding: 0; box-sizing: border-box; }
  html, body { width: 1200px; height: 852px; overflow: hidden; }
  body { background: var(--bg); position: relative; font-family: "Open Sans", Arial, sans-serif; }

  .card {
    position: absolute;
    width: 520px; height: 297px;
    background: var(--card);
    border-radius: 16px;
    overflow: hidden;
    box-shadow: 0 8px 22px rgba(0,0,0,.18);
  }
  .card--front { left: 60px; top: 140px; }
  .card--back  { left: 620px; top: 420px; }

  .card__swoosh { position: absolute; inset: 0; width: 100%; height: 100%; }

  .logo { position: absolute; display: flex; align-items: center; gap: 8px; white-space: nowrap; }
  .logo__dot { width: 12px; height: 12px; border-radius: 50%; background: var(--red); }
  .logo__name { font-family: "Oswald", "Arial Narrow", sans-serif; font-weight: 400; color: var(--red); line-height: 1; }
  .card--front .logo { left: 110px; top: 52px; }
  .card--front .logo__name { font-size: 50px; }
  .card--back .logo { left: 72px; top: 158px; }
  .card--back .logo__name { font-size: 28px; }

  .identity { position: absolute; text-align: right; }
  .identity__name { font-family: "Oswald", "Arial Narrow", sans-serif; color: var(--red); font-size: 17px; line-height: 1.1; }
  .identity__role { color: var(--text-grey); font-size: 12px; }
  .card--front .identity { right: 278px; top: 186px; }
  .card--back .identity { left: 298px; top: 56px; text-align: left; }

  .divider { position: absolute; width: 1px; background: var(--grey-light); }
  .card--front .divider { left: 254px; top: 160px; height: 100px; }
  .card--back .divider { left: 285px; top: 50px; height: 180px; }

  .contacts { position: absolute; list-style: none; font-size: 11.5px; color: var(--text-grey); }
  .contacts li { display: flex; align-items: center; gap: 7px; height: 21px; white-space: nowrap; }
  .card--front .contacts { left: 266px; top: 166px; }
  .card--back .contacts { left: 298px; top: 118px; }

  .icon { width: 13px; height: 13px; flex: none; }
</style>
</head>
<body>

<section class="card card--front" aria-label="business card front">
  <svg class="card__swoosh" viewBox="0 0 520 297" aria-hidden="true">
    <path d="M0 60 C40 140 90 230 210 297 L0 297 Z" fill="var(--red)"/>
    <path d="M0 40 C50 150 120 240 250 297" fill="none" stroke="var(--grey-light)" stroke-width="6"/>
    <path d="M0 60 C40 140 90 230 210 297" fill="none" stroke="var(--red-dark)" stroke-width="2"/>
  </svg>
  <div class="logo">
    <span class="logo__dot"></span>
    <span class="logo__name">marla verstegen</span>
  </div>
  <div class="identity">
    <div class="identity__name">marla verstegen</div>
    <div class="identity__role">professional chef</div>
  </div>
  <div class="divider"></div>
  <ul class="contacts">
    <li>
      <svg class="icon" viewBox="0 0 14 14"><circle cx="7" cy="7" r="7" fill="var(--red)"/><path d="M4.5 3.5 L6 5.5 L5.2 6.4 C5.8 7.6 6.5 8.3 7.6 8.8 L8.5 8 L10.5 9.5 L9.6 10.6 C7 10.3 3.8 7 3.5 4.4 Z" fill="#fff"/></svg>
      303.555.0142
    </li>
    <li>
      <svg class="icon" viewBox="0 0 14 14"><circle cx="7" cy="7" r="7" fill="var(--red)"/><circle cx="7" cy="7" r="1.8" fill="none" stroke="#fff" stroke-width="1.1"/><path d="M8.8 7 V8 C8.8 9.3 11 9.3 11 7.2 A4 4 0 1 0 9 10.5" fill="none" stroke="#fff" stroke-width="1.1"/></svg>
      marla@marlaverstegen.net
    </li>
    <li>
      <svg class="icon" viewBox="0 0 14 14"><circle cx="7" cy="7" r="7" fill="var(--pink)"/><circle cx="7" cy="7" r="3.6" fill="none" stroke="#fff" stroke-width="1"/><path d="M3.4 7 H10.6 M7 3.4 C5.5 5 5.5 9 7 10.6 C8.5 9 8.5 5 7 3.4" fill="none" stroke="#fff" stroke-width=".9"/></svg>
      marlaverstegen.net
    </li>
  </ul>
</section>

<section class="card card--back" aria-label="business card back">
  <svg class="card__swoosh" viewBox="0 0 520 297" aria-hidden="true">
    <path d="M0 40 C8 150 30 235 80 297 L0 297 Z" fill="var(--red)"/>
    <path d="M0 20 C15 150 55 240 125 297" fill="none" stroke="var(--grey-light)" stroke-width="6"/>
    <path d="M0 40 C8 150 30 235 80 297" fill="none" stroke="var(--red-dark)" stroke-width="2"/>
  </svg>
  <div class="logo">
    <span class="logo__dot"></span>
    <span class="logo__name">marla verstegen</span>
  </div>
  <div class="divider"></div>
  <div class="identity">
    <div class="identity__name">marla verstegen</div>
    <div class="identity__role">professional chef</div>
  </div>
  <ul class="contacts">
    <li>
      <svg class="icon" viewBox="0 0 14 14"><circle cx="7" cy="7" r="7" fill="var(--red)"/><path d="M4.5 3.5 L6 5.5 L5.2 6.4 C5.8 7.6 6.5 8.3 7.6 8.8 L8.5 8 L10.5 9.5 L9.6 10.6 C7 10.3 3.8 7 3.5 4.4 Z" fill="#fff"/></svg>
      303.555.0142
    </li>
    <li>
      <svg class="icon" viewBox="0 0 14 14"><circle cx="7" cy="7" r="7" fill="var(--red)"/><circle cx="7" cy="7" r="1.8" fill="none" stroke="#fff" stroke-width="1.1"/><path d="M8.8 7 V8 C8.8 9.3 11 9.3 11 7.2 A4 4 0 1 0 9 10.5" fill="none" stroke="#fff" stroke-width="1.1"/></svg>
      marla@marlaverstegen.net
    </li>
    <li>
      <svg class="icon" viewBox="0 0 14 14"><circle cx="7" cy="7" r="7" fill="var(--pink)"/><circle cx="7" cy="7" r="3.6" fill="none" stroke="#fff" stroke-width="1"/><path d="M3.4 7 H10.6 M7 3.4 C5.5 5 5.5 9 7 10.6 C8.5 9 8.5 5 7 3.4" fill="none" stroke="#fff" stroke-width=".9"/></svg>
      marlaverstegen.net
    </li>
  </ul>
</section>

</body>
</html>
```